Classy, Elegant, Simple Business Card Design

Looking to have a classy, simple, and elegant design. Want a top notch designed business card. I really like the look of the new brivo credit card. I also like the design I attached. I am trying to reach 21-29 year old females for booking us for there wedding or event. We offer Disc Jockey Service, Photo Booth Rentals, and Uplighting .

Target Market(s)

21-28 year old females

Contact Information for Business Card

Has to have logo, website, email, and phone number

Font styles to use
Other font styles liked:
• open to font choice, modern, clean
Designer to choose
33a6d7
0791cd
0555a3
ffffff

Requirements
Must have
• Has to have logo, website, email, and phone number
Nice to have
• I really like the design of the new brivo credit card. I also included my logo and some designs I like
Should not have
• clutter or too much info

```html
<!DOCTYPE html>
<html lang="en">
<head>
<meta charset="utf-8">
<title>Tidelight Event Group – Business Card</title>
<link rel="stylesheet" href="https://fonts.googleapis.com/css2?family=Montserrat:wght@400;500;700&display=swap">
<style>
  :root {
    --backdrop: #dcdcdc;
    --card: #f7f7f5;
    --navy: #0555a3;
    --blue: #0791cd;
    --sky: #33a6d7;
    --ink: #1f3f73;
    --grey: #9a9a9a;
    --emboss: #e9e9e6;
  }
  * { margin: 0; padding: 0; box-sizing: border-box; }
  html, body { width: 1200px; height: 800px; overflow: hidden; }
  body {
    background: var(--backdrop);
    font-family: "Montserrat", sans-serif;
    position: relative;
  }
  .card {
    position: absolute;
    top: 246px;
    width: 540px;
    height: 308px;
    background: var(--card);
  }
  .card--front { left: 40px; }
  .card--back { left: 620px; }

  .brand {
    position: absolute;
    display: flex;
    align-items: center;
    gap: 10px;
    color: var(--navy);
    font-weight: 500;
    text-transform: uppercase;
    letter-spacing: 2px;
    line-height: 1.15;
  }
  .brand__dot {
    width: 14px; height: 14px;
    border-radius: 50%;
    background: var(--blue);
    flex: none;
  }
  .card--front .brand { top: 40px; left: 300px; font-size: 17px; }
  .card--back .brand { bottom: 52px; left: 44px; font-size: 19px; }

  .emboss {
    position: absolute;
    right: 50px; top: 70px;
    width: 130px; height: 130px;
    border-radius: 50%;
    border: 3px solid var(--emboss);
  }

  .contact {
    position: absolute;
    left: 40px; bottom: 34px;
    color: var(--ink);
    font-size: 13px;
    line-height: 1.45;
  }
  .contact__name {
    font-size: 17px;
    letter-spacing: 1px;
    font-weight: 400;
    text-transform: uppercase;
  }
  .contact__name strong { color: var(--blue); font-weight: 700; }
  .contact__role { font-size: 13px; }
  .contact__rule {
    width: 72px; height: 1px;
    background: var(--ink);
    margin: 8px 0 10px;
  }
  .contact__line { display: flex; align-items: center; gap: 7px; }
  .contact__line svg { width: 11px; height: 11px; fill: var(--navy); flex: none; }
</style>
</head>
<body>
  <section class="card card--front">
    <div class="brand">
      <span class="brand__dot"></span>
      <span>Tidelight<br>Event Group</span>
    </div>
    <div class="contact">
      <p class="contact__name">Avery <strong>Lane</strong></p>
      <p class="contact__role">Manager</p>
      <div class="contact__rule"></div>
      <p>Your address, city<br>state, ZIP 0000</p>
      <p class="contact__line">
        <svg viewBox="0 0 24 24"><path d="M6.6 10.8a15.1 15.1 0 0 0 6.6 6.6l2.2-2.2c.3-.3.7-.4 1-.2 1.1.4 2.3.6 3.6.6.6 0 1 .4 1 1V20c0 .6-.4 1-1 1A17 17 0 0 1 3 4c0-.6.4-1 1-1h3.5c.6 0 1 .4 1 1 0 1.3.2 2.5.6 3.6.1.3 0 .7-.2 1z"/></svg>
        555-014-2100
      </p>
      <p class="contact__line">
        <svg viewBox="0 0 24 24"><path d="M2 5h20v14H2z M2 5l10 8 10-8" fill="none" stroke="#0555a3" stroke-width="2.4"/></svg>
        hello@tidelightevents.com
      </p>
      <p class="contact__line">
        <svg viewBox="0 0 24 24"><circle cx="12" cy="12" r="10" fill="none" stroke="#0555a3" stroke-width="2.4"/><path d="M2 12h20M12 2c3 3 3 17 0 20M12 2c-3 3-3 17 0 20" fill="none" stroke="#0555a3" stroke-width="1.8"/></svg>
        www.tidelightevents.com
      </p>
    </div>
  </section>

  <section class="card card--back">
    <div class="emboss"></div>
    <div class="brand">
      <span>Tidelight<br>Event Group</span>
    </div>
  </section>
</body>
</html>
```